Larkspur Ridge Management - Business Cards

I need business cards. My current logo was designed by a designer at this site and I very much like and am happy with the results. I would like a business card that is trendy, unique, current yet professional. I deal with high net worth clients daily

Target Market(s)

Out of state investors looking to get into the rental market in Ohio

Industry/Entity Type

Property Management, Consulting

Contact Information for Business Card

Name, Title (Chief Financial Officer) office phone number (555) 817-3094 website address larkridgemgmt.example

Font styles to use
Sans Serif

Colors
0054AA
0677BA
7BADD7
CADEEF
E8F1F8
0094D4
00A9DD
6FCCEA
C7EBF8
E9F6FB
00AB8E
00BBA5
67D7C9
C6EFE9
E9F9F6

```html
<!DOCTYPE html>
<html lang="en">
<head>
<meta charset="utf-8">
<title>Larkspur Ridge Management – Business Cards</title>
<link rel="stylesheet" href="https://fonts.googleapis.com/css2?family=Montserrat:wght@500;600;700;800&display=swap">
<style>
  :root {
    --brand-blue: #0054AA;
    --brand-blue-mid: #0677BA;
    --sky: #0094D4;
    --sky-bright: #00A9DD;
    --teal: #00AB8E;
    --teal-light: #00BBA5;
    --ink: #0054AA;
    --white: #ffffff;
    --page: #ffffff;
    --shadow: rgba(0, 0, 0, 0.35);
  }
  * { box-sizing: border-box; margin: 0; padding: 0; }
  html, body {
    width: 1200px;
    height: 1200px;
    overflow: hidden;
    background: var(--page);
    font-family: "Montserrat", Arial, sans-serif;
  }
  .sheet {
    position: relative;
    width: 1200px;
    height: 1200px;
  }
  .card {
    position: absolute;
    top: 470px;
    width: 447px;
    height: 261px;
    overflow: hidden;
    box-shadow: 6px 10px 18px var(--shadow);
  }
  /* Front */
  .card-front {
    left: 112px;
    background: var(--brand-blue);
  }
  .front-name {
    position: absolute;
    left: 0;
    right: 0;
    top: 104px;
    display: flex;
    align-items: center;
    justify-content: center;
    gap: 12px;
  }
  .front-name .mark {
    flex: none;
    width: 18px;
    height: 18px;
    background: var(--white);
  }
  .front-name .name {
    color: var(--white);
    font-weight: 700;
    font-size: 22px;
    line-height: 1.15;
    white-space: nowrap;
  }
  /* Back */
  .card-back {
    left: 661px;
    background: var(--white);
  }
  .person {
    position: absolute;
    left: 19px;
    top: 68px;
  }
  .person-name {
    color: var(--ink);
    font-weight: 700;
    font-size: 22px;
  }
  .person-title {
    color: var(--sky);
    font-weight: 500;
    font-size: 16px;
    margin-top: 3px;
  }
  .contacts {
    position: absolute;
    left: 19px;
    top: 139px;
    list-style: none;
  }
  .contacts li {
    display: flex;
    align-items: center;
    gap: 11px;
    color: var(--ink);
    font-weight: 600;
    font-size: 14px;
    height: 24px;
    white-space: nowrap;
  }
  .contacts svg { width: 13px; height: 13px; flex: none; }
  .back-name {
    position: absolute;
    right: 16px;
    top: 92px;
    width: 180px;
    display: flex;
    align-items: center;
    gap: 8px;
  }
  .back-name .mark {
    flex: none;
    width: 14px;
    height: 14px;
    background: var(--brand-blue);
  }
  .back-name .name {
    color: var(--ink);
    font-weight: 700;
    font-size: 17px;
    line-height: 1.15;
    white-space: nowrap;
  }
  .stripes {
    position: absolute;
    left: 0;
    bottom: 0;
    width: 447px;
    height: 60px;
  }
</style>
</head>
<body>
<main class="sheet">
  <section class="card card-front" aria-label="Card front">
    <div class="front-name">
      <span class="mark"></span>
      <span class="name">Larkspur Ridge<br>Management</span>
    </div>
  </section>

  <section class="card card-back" aria-label="Card back">
    <div class="person">
      <p class="person-name">Lorem ipsum</p>
      <p class="person-title">Chief Financial Officer</p>
    </div>
    <ul class="contacts">
      <li>
        <svg viewBox="0 0 16 16" aria-hidden="true"><circle cx="8" cy="8" r="8" fill="#00A9DD"/><path d="M5.2 4.2l1.3-.3.8 1.9-.9.7c.5 1 1.2 1.7 2.2 2.2l.7-.9 1.9.8-.3 1.3c-3.3.1-6-2.6-5.7-5.7z" fill="#fff"/></svg>
        (555) 817-3094
      </li>
      <li>
        <svg viewBox="0 0 16 16" aria-hidden="true"><circle cx="8" cy="8" r="8" fill="#00A9DD"/><circle cx="8" cy="8" r="4.2" fill="none" stroke="#fff" stroke-width="1"/><ellipse cx="8" cy="8" rx="1.8" ry="4.2" fill="none" stroke="#fff" stroke-width="1"/><line x1="3.8" y1="8" x2="12.2" y2="8" stroke="#fff" stroke-width="1"/></svg>
        larkridgemgmt.example
      </li>
    </ul>
    <div class="back-name">
      <span class="mark"></span>
      <span class="name">Larkspur Ridge<br>Management</span>
    </div>
    <svg class="stripes" viewBox="0 0 447 60" preserveAspectRatio="none" aria-hidden="true">
      <polygon points="0,60 447,0 447,60" fill="#00AB8E"/>
      <polygon points="170,60 330,36 345,36 200,60" fill="#ffffff"/>
      <polygon points="255,60 400,30 420,30 290,60" fill="#ffffff"/>
    </svg>
  </section>
</main>
</body>
</html>
```